Advertisement for back of sporting brochure

Company: Gridiron Ascent / gridascentpro.example
Business: Football skills development for offensive and defensive positions
Slogan: Learn to play the game on and off the field
Company colors: Royal Blue (reflex blue), White, Cool Gray 11 or Cool Gray 4, safety green can be used for some highlighting
Phone#: 555-283-9162

We require an 8.5" x 11" size flyer advertising the company.
The flyer will be displayed on the back of a sporting event program.
The objective of the flyer is to get viewers to contact Gridiron Ascent by either website or phone.

Must have items in the flyer are:
* Logo
* Slogan (see above)
* website (see above)
* Phone #
* photos
* Testimonials
* Word from the owner (see below)

“ In just 3 short years Gridiron Ascent clients have shown that skill development with the coaches at GA works! Over these past 3 years GA has had 24 players in the Continental Pigskin Circuit and 28 players go on to play at the collegiate level. We are making an impact on teams at every level including the 2013 High School State Championships with over 20 players participating in the state games. We have also worked with young players producing the MVP and Captains of the 2013 MRYL State champion. If you want to surround yourself with winners and raise your level of play while having fun and gaining confidence call us today!"

The CALL TO ACTION (CTA) is critical! The objective is for the viewer to call the phone number provided, now! The CTA should not fall into the same paragraph as information verbiage.

Target Market(s)

Elementary, Middle & High School players and parents

Industry/Entity Type

Advertising

Requirements
Must have
• CALL TO ACTION (CTA)
Readers must themselves, want to be part of the Gridiron Ascent family
OR
The parent must want their student athlete to become the best football player they can be
Should not have
• RED

```html
<!DOCTYPE html>
<html lang="en">
<head>
<meta charset="utf-8">
<title>Gridiron Ascent Flyer</title>
<link rel="stylesheet" href="https://fonts.googleapis.com/css2?family=Bebas+Neue&family=Alfa+Slab+One&family=Arimo:ital,wght@0,400;0,700;1,700&display=swap">
<style>
  :root {
    --page-bg: #e4e2df;
    --ink-black: #0b0b0e;
    --royal: #1c2a86;
    --royal-deep: #0c1446;
    --royal-band: #24339a;
    --silver-top: #ffffff;
    --silver-bottom: #9ea3aa;
    --cool-gray: #8a8d91;
    --white: #ffffff;
  }
  * { box-sizing: border-box; margin: 0; padding: 0; }
  html, body { width: 1200px; height: 857px; overflow: hidden; }
  body { background: var(--page-bg); position: relative; font-family: "Arimo", Arial, sans-serif; }

  .flyer {
    position: absolute; left: 321px; top: 68px; width: 558px; height: 722px;
    background: var(--ink-black); overflow: hidden;
    box-shadow: 0 6px 18px rgba(0,0,0,.25);
  }

  .brand {
    position: absolute; top: 38px; left: 0; width: 100%;
    display: flex; justify-content: center; align-items: center; gap: 10px;
  }
  .brand-dot { width: 14px; height: 14px; border-radius: 50%; background: var(--royal-band); }
  .brand-name {
    font-family: "Bebas Neue", Impact, sans-serif; font-size: 34px; letter-spacing: 2px;
    color: var(--royal-band); line-height: 1;
  }

  .slogan {
    position: absolute; top: 108px; left: 0; width: 100%; text-align: center;
    font-family: "Bebas Neue", Impact, sans-serif; font-size: 46px; line-height: 44px;
    letter-spacing: 4px; color: #d6d8db;
    background: linear-gradient(var(--silver-top), var(--silver-bottom));
    -webkit-background-clip: text; background-clip: text; -webkit-text-fill-color: transparent;
  }

  .team-photo {
    position: absolute; top: 195px; left: 0; width: 100%; height: 168px;
    background: linear-gradient(180deg, #9a9a9a 0%, #c9c9c9 30%, #6d6d6d 65%, #3f3f3f 100%);
  }

  .info-panel {
    position: absolute; top: 363px; left: 0; width: 100%; height: 306px;
    background: linear-gradient(180deg, var(--royal) 0%, #16227a 45%, var(--royal-deep) 100%);
  }

  .drill-photo {
    position: absolute; top: -8px; left: 22px; width: 134px; height: 134px; border-radius: 50%;
    border: 5px solid var(--white);
    background: radial-gradient(circle at 50% 40%, #d8d8d8 0%, #9c9c9c 55%, #555 100%);
    box-shadow: 0 6px 10px rgba(0,0,0,.45);
  }

  .section-title {
    font-family: "Alfa Slab One", Georgia, serif; font-size: 13px; letter-spacing: 1px;
    color: var(--white); line-height: 1;
  }
  .about { position: absolute; top: 10px; left: 188px; width: 344px; }
  .about p {
    margin-top: 5px; font-size: 9px; line-height: 11.3px; color: #e6e8f2; text-align: justify;
  }
  .testimonial { position: absolute; top: 123px; left: 188px; width: 344px; }
  .testimonial .quote {
    margin-top: 5px; font-size: 8.6px; line-height: 11.5px; color: var(--white); font-weight: 700;
  }
  .testimonial .author { margin-top: 14px; font-size: 8.4px; color: #e6e8f2; line-height: 12px; }
  .testimonial .role { font-size: 8.4px; font-weight: 700; font-style: italic; color: var(--white); }

  .cta {
    position: absolute; top: 219px; left: 0; width: 100%; height: 80px;
    background: linear-gradient(90deg, rgba(36,51,154,.1) 0%, var(--royal-band) 60%, var(--royal-band) 100%);
    text-align: right; padding: 7px 28px 0 0;
  }
  .cta p { font-size: 10.6px; line-height: 12.5px; color: #e6e8f2; }
  .cta strong { color: var(--white); }
  .phone {
    display: block; margin-top: 6px; font-size: 33px; font-weight: 700; color: var(--white);
    letter-spacing: .5px; line-height: 1;
  }

  .website {
    position: absolute; bottom: 18px; right: 30px;
    font-family: Georgia, "Times New Roman", serif; font-size: 12px; letter-spacing: 3.5px; color: #d4d6da;
  }
</style>
</head>
<body>
  <main class="flyer">
    <header class="brand">
      <span class="brand-dot"></span>
      <span class="brand-name">Gridiron Ascent</span>
    </header>

    <h1 class="slogan">LEARN TO PLAY THE GAME<br>ON AND OFF THE FIELD</h1>

    <div class="team-photo" role="img" aria-label="Black and white group photo of players and coaches at an indoor training facility"></div>

    <section class="info-panel">
      <div class="drill-photo" role="img" aria-label="Circular photo of a player running a footwork drill over pads"></div>

      <div class="about">
        <h2 class="section-title">ABOUT US</h2>
        <p>In just 3 short years Gridiron Ascent clients have shown that skill development with the coaches at GA works! Over these past 3 years GA has had 24 players in the Continental Pigskin Circuit and 28 players go on to play at the collegiate level. We are making an impact on teams at every level including the 2013 High School State Championships with over 20 players participating in the state games. We have also worked with young players producing the MVP and Captains of the 2013 MRYL State champion.</p>
      </div>

      <div class="testimonial">
        <h2 class="section-title">TESTIMONIAL</h2>
        <p class="quote">I've known Marcus Hale most of my nearly 20 year coaching career. In a profession where you stress character, honesty, loyalty, commitment and determination, it has been truly an honor...</p>
        <p class="author">Owen Castell</p>
        <p class="role">Assistant Football Coach - Lakeshore Crest University</p>
      </div>

      <div class="cta">
        <p>If you want to surround yourself with winners and raise your level of play<br>while having fun and gaining confidence<br><strong>call us today!</strong></p>
        <span class="phone">555-283-9162</span>
      </div>
    </section>

    <p class="website">www.gridascentpro.example</p>
  </main>
</body>
</html>
```